Dalton Power Supply, Inc. Business Card Design

We are an Electrical Distributor looking for a Modern, Professional Business Card design.

Target Market(s)

Residential Commercial Industrial

Industry/Entity Type

Electrical

Contact Information for Business Card

Dalton Power Supply, Inc.
418 Maple Ridge Lane
Brookvale, NC 27514
555-214-7630
555-214-8842 Fax
daltonpower@brightmail-example.net

```html
<!DOCTYPE html>
<html lang="en">
<head>
<meta charset="utf-8">
<title>Dalton Power Supply, Inc. — Business Card</title>
<link href="https://fonts.googleapis.com/css2?family=Arimo:wght@400;700&display=swap" rel="stylesheet">
<style>
  :root {
    --bg: #d4d4d4;
    --red: #be102d;
    --charcoal: #333333;
    --white: #ffffff;
    --ink: #111111;
    --text-dark: #2a2a2a;
    --blue: #3b8ee0;
  }
  * { margin: 0; padding: 0; box-sizing: border-box; }
  html, body { width: 1200px; height: 1200px; overflow: hidden; }
  body { background: var(--bg); font-family: "Arimo", Arial, sans-serif; position: relative; }

  /* Front */
  .card-front { position: absolute; left: 182px; top: 97px; width: 862px; height: 460px; }
  .front-edge { position: absolute; left: 0; top: 0; width: 60px; height: 460px; background: var(--red); border-radius: 42px 0 0 42px; }
  .front-spine { position: absolute; left: 42px; top: 0; width: 72px; height: 460px; background: var(--white); }
  .spine-name {
    position: absolute; left: 76px; top: 230px;
    transform: translate(-50%, -50%) rotate(-90deg);
    white-space: nowrap; color: var(--red); font-weight: 700; font-size: 24px;
  }
  .front-hero { position: absolute; left: 114px; top: 0; width: 748px; height: 298px; background: var(--red); }
  .hero-title { position: absolute; left: 79px; top: 52px; font-size: 39px; font-weight: 700; color: var(--ink); white-space: nowrap; }
  .hero-mark { position: absolute; left: 327px; top: 146px; }
  .front-contact { position: absolute; left: 114px; top: 298px; width: 748px; height: 162px; background: var(--charcoal); }
  .contact-row { position: absolute; left: 29px; display: flex; align-items: center; gap: 10px; color: var(--ink); font-size: 25px; font-weight: 700; white-space: nowrap; }
  .contact-row svg { width: 22px; height: 22px; flex: none; }
  .row-address { top: 33px; }
  .row-phone { top: 74px; }
  .row-email { top: 115px; }

  /* Back */
  .card-back { position: absolute; left: 182px; top: 672px; width: 862px; height: 477px; background: var(--white); overflow: hidden; }
  .back-band { position: absolute; left: 0; top: 259px; width: 862px; height: 218px; background: var(--blue); }
  .band-notch { position: absolute; left: 64px; top: 259px; width: 725px; height: 18px; background: var(--white); }
  .info-col { position: absolute; top: 40px; text-align: left; color: var(--text-dark); font-weight: 700; font-size: 14.5px; }
  .info-icon { display: block; }
  .col-email { left: 36px; }
  .col-email .info-icon { margin-left: 115px; }
  .col-phone { left: 368px; }
  .col-phone .info-icon { margin-left: -5px; }
  .col-address { left: 604px; }
  .col-address .info-icon { margin-left: 40px; }
  .info-text { position: absolute; white-space: nowrap; }
  .back-brand { position: absolute; left: 78px; top: 307px; display: flex; align-items: center; gap: 28px; }
  .brand-ring { width: 132px; height: 132px; border: 12px solid var(--ink); border-radius: 50%; flex: none; }
  .brand-name { font-size: 44px; font-weight: 700; color: var(--ink); white-space: nowrap; }
</style>
</head>
<body>

<section class="card-front">
  <div class="front-edge"></div>
  <div class="front-spine"></div>
  <div class="spine-name">Dalton Power Supply, Inc.</div>
  <div class="front-hero">
    <h1 class="hero-title">Dalton Power Supply, Inc.</h1>
    <svg class="hero-mark" width="96" height="96" viewBox="0 0 96 96" aria-label="Dalton Power Supply mark">
      <circle cx="48" cy="48" r="40" fill="none" stroke="var(--ink)" stroke-width="10"/>
    </svg>
  </div>
  <div class="front-contact">
    <div class="contact-row row-address">
      <svg viewBox="0 0 24 24"><path d="M12 2a7 7 0 0 0-7 7c0 5 7 13 7 13s7-8 7-13a7 7 0 0 0-7-7zm0 4a3 3 0 1 1 0 6 3 3 0 0 1 0-6z" fill="var(--red)"/></svg>
      <span>418 Maple Ridge Lane Brookvale, NC 27514</span>
    </div>
    <div class="contact-row row-phone">
      <svg viewBox="0 0 24 24"><path d="M2 9c0-3 20-3 20 0v2h-5V9H7v2H2zM7 12h10l3 7H4z" fill="var(--red)"/><circle cx="12" cy="15.5" r="2" fill="var(--charcoal)"/></svg>
      <span>555-214-7630 &nbsp;&amp; Fax : 555-214-8842</span>
    </div>
    <div class="contact-row row-email">
      <svg viewBox="0 0 24 24"><rect x="2" y="5" width="20" height="14" rx="1" fill="var(--red)"/><path d="M2 6l10 7 10-7" fill="none" stroke="var(--charcoal)" stroke-width="1.6"/></svg>
      <span>daltonpower@brightmail-example.net</span>
    </div>
  </div>
</section>

<section class="card-back">
  <div class="info-col col-email">
    <svg class="info-icon" width="86" height="56" viewBox="0 0 86 56"><rect x="0" y="0" width="86" height="56" rx="5" fill="var(--text-dark)"/><path d="M3 3l40 28 40-28" fill="none" stroke="var(--white)" stroke-width="4"/></svg>
    <span class="info-text" style="top:112px;left:0">daltonpower@brightmail-example.net</span>
  </div>
  <div class="info-col col-phone">
    <svg class="info-icon" width="92" height="66" viewBox="0 0 92 66"><path d="M2 18C2 2 90 2 90 18v9H68v-10H24v10H2z" fill="var(--text-dark)"/><path d="M26 22h40l12 44H14z" fill="var(--text-dark)"/><g fill="var(--white)"><rect x="36" y="34" width="5" height="4"/><rect x="44" y="34" width="5" height="4"/><rect x="52" y="34" width="5" height="4"/><rect x="36" y="41" width="5" height="4"/><rect x="44" y="41" width="5" height="4"/><rect x="52" y="41" width="5" height="4"/><rect x="36" y="48" width="5" height="4"/><rect x="44" y="48" width="5" height="4"/><rect x="52" y="48" width="5" height="4"/></g></svg>
    <span class="info-text" style="top:112px;left:0">555 214 7630</span>
    <span class="info-text" style="top:153px;left:0">555 214 8842</span>
  </div>
  <div class="info-col col-address">
    <svg class="info-icon" width="90" height="74" viewBox="0 0 90 74"><path d="M4 36L45 4l41 32" fill="none" stroke="var(--text-dark)" stroke-width="6"/><rect x="64" y="8" width="9" height="16" fill="var(--text-dark)"/><path d="M14 38L45 14l31 24v32a4 4 0 0 1-4 4H55V56a10 10 0 0 0-20 0v18H18a4 4 0 0 1-4-4z" fill="var(--text-dark)"/></svg>
    <span class="info-text" style="top:116px;left:0">418 Maple Ridge Lane</span>
    <span class="info-text" style="top:157px;left:0">Brookvale, NC 27514</span>
  </div>

  <div class="back-band"></div>
  <div class="band-notch"></div>
  <div class="back-brand">
    <div class="brand-ring"></div>
    <div class="brand-name">Dalton Power Supply, Inc.</div>
  </div>
</section>

</body>
</html>
```